Thank you for shopping with us business card

We would like a thank you card for our rebranded business. We used to be "Kestrel Knacks" but are now "Kestrel Trinkets. Old thank you card and new logo will be attached for reference. New thank you card does not have to be same design as old thank you card, but please use new logo.
Mopsa URL is now kestreltrinkets.mopsa.com
Pictaloo is @Kestrel_Trinkets
Email is kestreltrinkets@mopsamail.com
Thank you!

Contact Information for Business Card

Mopsa site, email, Pictaloo

```html
<!DOCTYPE html>
<html lang="en">
<head>
<meta charset="utf-8">
<title>Kestrel Trinkets – Thank You Card</title>
<link rel="stylesheet" href="https://fonts.googleapis.com/css2?family=Montserrat:wght@500;600;700&family=Open+Sans:wght@400;600&display=swap">
<style>
  :root {
    --page-bg: #2b2d31;
    --card-white: #ffffff;
    --brand-purple: #8e5fab;
    --brand-purple-deep: #7f4ea3;
    --ink: #111111;
    --ink-soft: #555555;
    --rule: #222222;
  }
  * { box-sizing: border-box; margin: 0; padding: 0; }
  html, body {
    width: 1200px; height: 952px; overflow: hidden;
    background: var(--page-bg);
  }
  .canvas {
    position: relative; width: 1200px; height: 952px;
    display: flex; flex-direction: column; align-items: center; justify-content: center; gap: 56px;
  }
  .card {
    position: relative; width: 700px; height: 400px;
    box-shadow: 0 10px 30px rgba(0,0,0,.4);
    overflow: hidden;
  }
  /* Front */
  .card--front { background: var(--card-white); }
  .contact-list {
    position: absolute; left: 48px; top: 120px;
    list-style: none; display: flex; flex-direction: column; gap: 9px;
    font-family: "Open Sans", sans-serif; font-size: 15px; color: var(--ink-soft);
  }
  .contact-list li { display: flex; align-items: center; gap: 9px; }
  .contact-icon {
    width: 18px; height: 18px; border-radius: 3px; background: var(--brand-purple);
    display: inline-flex; align-items: center; justify-content: center; flex: none;
  }
  .brand-lockup {
    position: absolute; right: 60px; top: 88px;
    display: flex; align-items: center; gap: 18px;
  }
  .brand-mark { width: 44px; height: 44px; background: var(--ink); }
  .brand-divider { width: 2px; height: 70px; background: var(--rule); }
  .brand-name {
    font-family: "Montserrat", sans-serif; font-weight: 600; font-size: 27px;
    line-height: 1.05; letter-spacing: .04em; text-transform: uppercase; color: var(--ink);
  }
  .thanks-banner {
    position: absolute; right: 0; top: 214px; width: 390px; height: 78px;
    background: var(--brand-purple); border-radius: 18px 0 0 0;
    padding: 10px 30px 0 0; text-align: right;
    font-family: "Montserrat", sans-serif; font-weight: 700; font-size: 24px;
    line-height: 1.1; color: #fff; text-transform: uppercase;
  }
  .thanks-message {
    position: absolute; right: 30px; top: 302px; width: 360px; text-align: right;
    font-family: "Open Sans", sans-serif; font-size: 14px; line-height: 1.4; color: var(--ink-soft);
  }
  /* Back */
  .card--back { background: var(--brand-purple); }
  .back-name {
    position: absolute; left: 0; right: 0; top: 50%; transform: translateY(-50%);
    text-align: center;
    font-family: "Montserrat", sans-serif; font-weight: 500; font-size: 34px;
    letter-spacing: .03em; text-transform: uppercase; color: #fff;
  }
</style>
</head>
<body>
<main class="canvas">
  <section class="card card--front" aria-label="Card front">
    <ul class="contact-list">
      <li><span class="contact-icon" aria-hidden="true"></span>kestreltrinkets.mopsa.com</li>
      <li><span class="contact-icon" aria-hidden="true"></span>@Kestrel_Trinkets</li>
      <li>
        <span class="contact-icon" aria-hidden="true">
          <svg width="12" height="9" viewBox="0 0 12 9"><rect x="0.5" y="0.5" width="11" height="8" fill="none" stroke="#fff"/><path d="M0.5 0.5 L6 5 L11.5 0.5" fill="none" stroke="#fff"/></svg>
        </span>kestreltrinkets@mopsamail.com
      </li>
    </ul>
    <div class="brand-lockup">
      <span class="brand-mark" aria-hidden="true"></span>
      <span class="brand-divider" aria-hidden="true"></span>
      <span class="brand-name">Kestrel<br>Trinkets</span>
    </div>
    <div class="thanks-banner">Thank you<br>for your purchase</div>
    <p class="thanks-message">Your purchase made my day and I hope this package brightens yours. Please come back and leave a review!</p>
  </section>
  <section class="card card--back" aria-label="Card back">
    <p class="back-name">Kestrel Trinkets</p>
  </section>
</main>
</body>
</html>
```